Folder Design: Mobile Laboratory Service

Need a folder designed for a Mobile Laboratory Service. Folder needs to be very professional and will be used to hold brochure, contract and business card of business. Logos of the company are attached.

Industry/Entity Type

Healthcare

```html
<!DOCTYPE html>
<html lang="en">
<head>
<meta charset="utf-8">
<title>Roving Clinical Labs – Presentation Folder</title>
<link rel="stylesheet" href="https://fonts.googleapis.com/css2?family=Cinzel:wght@600;700&family=Poppins:wght@400;600&display=swap">
<style>
  :root {
    --backdrop: #dde3e6;
    --paper: #ffffff;
    --navy: #061225;
    --navy-deep: #030b18;
    --navy-pocket: #0a1c36;
    --blue: #2f80e4;
    --blue-light: #7ab4f0;
    --ice: #cfe3f7;
    --blush: #f3dcec;
    --text-light: #ffffff;
  }
  * { margin: 0; padding: 0; box-sizing: border-box; }
  html, body { width: 677px; height: 1200px; overflow: hidden; background: var(--backdrop); }
  .canvas { width: 677px; height: 1200px; display: flex; align-items: center; justify-content: center; }
  .folder { width: 607px; height: 525px; display: block; filter: drop-shadow(0 4px 8px rgba(0,0,0,.25)); }
  .brand-title { font-family: "Cinzel", serif; font-weight: 700; }
  .brand-name { font-family: "Cinzel", serif; font-weight: 600; }
  .contact { font-family: "Poppins", sans-serif; font-weight: 400; }
  .web { font-family: "Poppins", sans-serif; letter-spacing: 3px; }
  .web-strong { font-weight: 600; fill: var(--blue); }
</style>
</head>
<body>
<main class="canvas">
  <svg class="folder" viewBox="0 0 1168 1010" xmlns="http://www.w3.org/2000/svg">
    <defs>
      <linearGradient id="lab-photo-tone" x1="0" y1="0" x2="0" y2="1">
        <stop offset="0" stop-color="var(--blush)" stop-opacity=".7"/>
        <stop offset=".5" stop-color="var(--ice)"/>
        <stop offset="1" stop-color="#7fb6ea"/>
      </linearGradient>
      <linearGradient id="lab-photo-fade" x1="0" y1="0" x2="1" y2="0">
        <stop offset="0" stop-color="#fff" stop-opacity="1"/>
        <stop offset=".45" stop-color="#fff" stop-opacity="0"/>
      </linearGradient>
      <linearGradient id="arc-band" x1="0" y1="0" x2="1" y2="0">
        <stop offset="0" stop-color="var(--blue-light)"/>
        <stop offset="1" stop-color="var(--blue)"/>
      </linearGradient>
      <radialGradient id="beaker-tone" cx=".6" cy=".75" r=".55">
        <stop offset="0" stop-color="#1a3a66" stop-opacity=".55"/>
        <stop offset="1" stop-color="#1a3a66" stop-opacity="0"/>
      </radialGradient>
      <radialGradient id="icon-fill" cx=".4" cy=".35" r=".7">
        <stop offset="0" stop-color="#6fb0f5"/>
        <stop offset="1" stop-color="#1f6fd6"/>
      </radialGradient>
    </defs>

    <!-- pockets -->
    <g class="pocket-left">
      <path d="M37 780 L585 780 L548 1010 L37 1010 L0 988 L0 798 Z" fill="var(--navy-pocket)"/>
      <text class="web" x="310" y="888" transform="rotate(180 310 888)" text-anchor="middle" font-size="16" fill="var(--text-light)">www.<tspan class="web-strong">rovingclinicallabs</tspan>.com</text>
    </g>
    <g class="pocket-right">
      <path d="M588 780 L1131 780 L1168 798 L1168 988 L1131 1010 L626 1010 Z" fill="var(--navy-pocket)"/>
      <g transform="rotate(180 860 888)">
        <circle cx="860" cy="860" r="34" fill="none" stroke="var(--blue)" stroke-width="5"/>
        <text class="brand-name" x="860" y="925" text-anchor="middle" font-size="15" fill="var(--blue)">Roving Clinical Labs</text>
      </g>
    </g>

    <!-- main cover panel -->
    <g class="cover">
      <rect x="37" y="0" width="1094" height="790" fill="var(--paper)"/>
      <rect x="820" y="0" width="311" height="600" fill="url(#lab-photo-tone)" role="img" aria-label="Photograph of glass test tubes in a rack"/>
      <rect x="820" y="0" width="311" height="600" fill="url(#lab-photo-fade)"/>

      <path d="M37 560 Q584 -30 1131 560 L1131 575 Q584 0 37 575 Z" fill="url(#arc-band)"/>
      <path d="M37 575 Q584 0 1131 575 L1131 790 L37 790 Z" fill="var(--navy)"/>
      <path d="M37 575 Q584 0 1131 575 L1131 790 L37 790 Z" fill="url(#beaker-tone)" role="img" aria-label="Dark toned photograph of a laboratory beaker"/>

      <!-- top logo stand-in -->
      <g class="brand-mark">
        <circle cx="740" cy="150" r="62" fill="none" stroke="var(--blue)" stroke-width="5"/>
        <text class="brand-name" x="740" y="245" text-anchor="middle" font-size="18" fill="var(--blue)">Roving Clinical Labs</text>
      </g>

      <!-- badge stand-in -->
      <g class="brand-badge">
        <circle cx="320" cy="363" r="76" fill="var(--navy)" stroke="#c9def5" stroke-width="6"/>
        <text class="brand-name" x="320" y="357" text-anchor="middle" font-size="15" fill="var(--blue-light)">Roving</text>
        <text class="brand-name" x="320" y="377" text-anchor="middle" font-size="15" fill="var(--blue-light)">Clinical Labs</text>
      </g>

      <!-- contact icons -->
      <g class="contact-icons">
        <line x1="206" y1="503" x2="236" y2="503" stroke="var(--blue)" stroke-width="2"/>
        <line x1="402" y1="503" x2="434" y2="503" stroke="var(--blue)" stroke-width="2"/>
        <circle cx="252" cy="503" r="15" fill="url(#icon-fill)"/>
        <path d="M252 512 C246 504 246 502 246 499 A6 6 0 0 1 258 499 C258 502 258 504 252 512 Z" fill="var(--navy)"/>
        <circle cx="252" cy="499" r="2" fill="#6fb0f5"/>
        <circle cx="295" cy="503" r="15" fill="url(#icon-fill)"/>
        <path d="M289 495 l4 -1 3 6 -2 2 c1 3 3 5 6 6 l2 -2 6 3 -1 4 c-10 0 -18 -8 -18 -18 Z" fill="var(--navy)"/>
        <circle cx="340" cy="503" r="15" fill="url(#icon-fill)"/>
        <rect x="332" y="497" width="16" height="12" rx="1" fill="var(--navy)"/>
        <path d="M332 497 L340 504 L348 497" fill="none" stroke="#6fb0f5" stroke-width="1.5"/>
        <circle cx="386" cy="503" r="15" fill="url(#icon-fill)"/>
        <g fill="none" stroke="var(--navy)" stroke-width="1.8">
          <circle cx="386" cy="503" r="8"/>
          <ellipse cx="386" cy="503" rx="3.5" ry="8"/>
          <line x1="378" y1="503" x2="394" y2="503"/>
        </g>
      </g>

      <!-- contact details -->
      <g class="contact" fill="var(--text-light)" font-size="13" text-anchor="middle">
        <text x="320" y="569">23456 Lorem Ipsum City</text>
        <text x="320" y="584">lorem Ipsum 767676</text>
        <text x="320" y="614">555 0142 7788</text>
        <text x="320" y="642">hello@rovingclinicallabs.com</text>
        <text x="320" y="672">www.rovingclinicallabs.com</text>
      </g>

      <!-- title -->
      <g class="brand-title">
        <text x="643" y="506" font-size="50" fill="var(--blue)">ROVING</text>
        <text x="643" y="553" font-size="50" fill="var(--text-light)">CLINICAL</text>
        <text x="643" y="600" font-size="50" fill="var(--text-light)">LABS</text>
      </g>
      <line x1="643" y1="631" x2="825" y2="631" stroke="#8a96a8" stroke-width="1"/>
      <line x1="680" y1="631" x2="710" y2="631" stroke="var(--text-light)" stroke-width="4"/>
      <text class="web" x="643" y="672" font-size="16" fill="var(--text-light)">www.<tspan class="web-strong">rovingclinicallabs</tspan>.com</text>
    </g>
  </svg>
</main>
</body>
</html>
```